Webdesign für  IT-Dienstleistungen
Webdesign für IT-Dienstleistungen
Zielgruppe
Wir bieten IT-Dienstleistungen rund um Handy, PC, Laptop und ZEP.
Zielgruppe sind Privatkunden im unterschiedlichen Alter, die Beratung benötigen oder Probleme haben.
Die Leute werden teilweise nicht super IT-affin sein, also muss das Design gut und die usability einfach sein.
Aufgabenstellung
Anbei sind Logo und Visual die bereits erstellt wurden und verwendet werden können.
Inhalte von https://dev.vameko.com/start/ und https://dev.vameko.com/anfrage/ und das anmeldeformular: https://dev.vameko.com/mein-konto/ soll auch auf der Startseite ersichtlich sein
sollten die Startseite ergeben plus Bilder und Texte, wo auch Konversation mit dem Kunden angezeigt werden kann, wenn eingeloggt.
Die Seite sollte sowohl auf dem barrierearm und responsive sein.

```html
<!DOCTYPE html>
<html lang="de">
<head>
<meta charset="utf-8">
<title>Vameko – Ihre Hotline bei Technikproblemen</title>
<link href="https://fonts.googleapis.com/css2?family=Mulish:wght@400;600;700&display=swap" rel="stylesheet">
<style>
  :root {
    --green: #84a514;
    --grey-text: #7a7a7a;
    --grey-dark: #6e7072;
    --topbar-bg: #f5f5f5;
    --white: #ffffff;
  }
  * { margin: 0; padding: 0; box-sizing: border-box; }
  html, body { width: 1200px; height: 617px; overflow: hidden; }
  body { font-family: "Mulish", Arial, sans-serif; background: var(--white); position: relative; }

  .topbar { position: absolute; left: 0; top: 0; width: 1200px; height: 35px; background: var(--topbar-bg); }
  .contact-item { position: absolute; top: 5px; display: flex; align-items: center; color: var(--grey-text); }
  .contact-icon { width: 24px; height: 24px; border-radius: 50%; background: var(--green); display: flex; align-items: center; justify-content: center; margin-right: 9px; }
  .contact-phone { left: 404px; font-size: 14px; font-weight: 600; letter-spacing: .2px; }
  .contact-mail { left: 621px; font-size: 12px; font-weight: 600; }
  .contact-mail .contact-icon { margin-right: 7px; }

  .site-header { position: absolute; left: 0; top: 35px; width: 1200px; height: 98px; background: var(--white); }
  .brand { position: absolute; left: 172px; top: 32px; font-size: 30px; font-weight: 700; color: var(--grey-dark); letter-spacing: 1px; line-height: 1; }
  .main-nav { position: absolute; top: 52px; left: 0; width: 100%; }
  .main-nav a { position: absolute; font-size: 12.5px; font-weight: 700; color: var(--grey-text); text-decoration: none; white-space: nowrap; }
  .main-nav a.active { color: var(--green); }
  .main-nav a.active::after { content: ""; position: absolute; left: -7px; right: -7px; top: 20px; height: 2px; background: var(--green); }

  .hero { position: absolute; left: 0; top: 133px; width: 1200px; height: 484px; overflow: hidden; }
  .hero-visual { position: absolute; inset: 0;
    background:
      radial-gradient(ellipse 300px 380px at 760px 300px, #f3f3f1 0%, rgba(243,243,241,0) 70%),
      linear-gradient(90deg, #eef0f0 0%, #e9ecec 40%, #e6e9e9 60%, #dfe6ea 85%, #d3e0e6 100%); }
  .hero-content { position: absolute; left: 200px; top: 151px; }
  .hero-title { color: var(--green); font-weight: 700; line-height: 1; }
  .hero-title .line-main { display: block; font-size: 38px; }
  .hero-title .line-sub { display: block; font-size: 27px; margin-top: 6px; }
  .hero-text { margin-top: 24px; font-size: 18px; line-height: 27px; color: var(--grey-text); width: 520px; }
  .hero-sign { margin-top: 27px; font-size: 18px; line-height: 27px; color: var(--grey-text); }
  .hero-sign strong { font-weight: 700; color: var(--grey-dark); }
</style>
</head>
<body>
  <div class="topbar">
    <div class="contact-item contact-phone">
      <span class="contact-icon">
        <svg width="10" height="14" viewBox="0 0 10 14"><rect x="1" y="0.5" width="8" height="13" rx="1.5" fill="#fff"/><rect x="2.5" y="2" width="5" height="8" fill="#84a514"/><circle cx="5" cy="11.7" r=".8" fill="#84a514"/></svg>
      </span>
      Telefon: 0041615550187
    </div>
    <div class="contact-item contact-mail">
      <span class="contact-icon">
        <svg width="12" height="9" viewBox="0 0 12 9"><rect width="12" height="9" rx="1" fill="#fff"/><path d="M0.5 1 L6 5 L11.5 1" stroke="#84a514" stroke-width="1.2" fill="none"/></svg>
      </span>
      E-Mail: support@vameko.com
    </div>
  </div>

  <header class="site-header">
    <div class="brand">VAMEKO</div>
    <nav class="main-nav">
      <a class="active" href="#" style="left:510px">START</a>
      <a href="#" style="left:567px">ANFRAGE</a>
      <a href="#" style="left:643px">WIE FUNKTIONIERT ES?</a>
      <a href="#" style="left:803px">PREISE</a>
      <a href="#" style="left:865px">FIRMENKUNDE</a>
      <a href="#" style="left:971px">MEIN KONTO</a>
    </nav>
  </header>

  <section class="hero">
    <div class="hero-visual" role="img" aria-label="Foto: Support-Mitarbeiter mit Headset am Computer, hell überblendet"></div>
    <div class="hero-content">
      <h1 class="hero-title">
        <span class="line-main">Willkommen bei Vameko -</span>
        <span class="line-sub">ihrer Hotline bei Technikproblemen</span>
      </h1>
      <p class="hero-text">Unser Ziel ist es unabhängigen Technikberatung für alle Interessenten zu bieten und eine schnelle und transpartente Unterstützung bei Problemfällen zu bieten.</p>
      <p class="hero-sign">Im Namen des VAMEKO Teams,<br><strong>Daniel, Christoph und Patrick</strong></p>
    </div>
  </section>
</body>
</html>
```